Divorce Lawyer print and ebook cover (Planting gardens after every storm )

I need a front and back cover for my divorce and family law book. I already have a photo and title. The back cover photo is not necessary but can be interesting the Front-main cover is a must

Target Market(s)

Prospective client

Colors

Designer to choose colors to be used in the design.

Requirements
Must have
• Front photo by viewable.

```html
<!DOCTYPE html>
<html lang="en">
<head>
<meta charset="utf-8">
<title>Planting Gardens After Every Storm – Cover Wrap</title>
<link rel="stylesheet" href="https://fonts.googleapis.com/css2?family=Cinzel:wght@400&family=EB+Garamond:wght@400&family=Allura&display=swap">
<style>
  :root {
    --ink: #000000;
    --paper: #ffffff;
    --body-text: #f2efe6;
    --gold-light: #e6d6a6;
    --gold-mid: #c9a86a;
    --gold-deep: #8a6a3a;
    --spine-dark: #3a2a14;
    --spine-mid: #6e5734;
    --spine-light: #8c7248;
    --band-light: #d8c394;
    --band-dark: #7a6034;
    --title-ink: #111008;
  }
  * { margin: 0; padding: 0; box-sizing: border-box; }
  html, body { width: 1200px; height: 830px; overflow: hidden; background: var(--ink); }
  .cover-wrap { position: relative; width: 1200px; height: 830px; background: var(--ink); }

  /* Back cover */
  .back-cover { position: absolute; left: 0; top: 0; width: 555px; height: 830px; background: var(--ink); }
  .back-copy {
    position: absolute; left: 50px; width: 441px;
    font-family: "EB Garamond", Georgia, serif;
    font-size: 14px; line-height: 18.4px; color: var(--body-text);
    text-align: justify; hyphens: auto;
  }
  .back-copy.intro { top: 86px; }
  .back-copy.details { top: 270px; }
  .back-copy.about { top: 446px; left: 217px; width: 274px; height: 148px; overflow: hidden; }
  .author-photo { position: absolute; left: 48px; top: 449px; width: 151px; height: 154px; background: var(--paper); }
  .isbn-block { position: absolute; left: 346px; top: 698px; width: 152px; height: 86px; background: var(--paper); }

  /* Spine */
  .spine {
    position: absolute; left: 555px; top: 0; width: 88px; height: 830px;
    background: linear-gradient(90deg, var(--spine-dark), var(--spine-light) 45%, var(--spine-mid) 80%, var(--spine-dark));
  }
  .spine-text {
    position: absolute; left: 50%; top: 50%;
    transform: translate(-50%, -50%) rotate(-90deg);
    width: 800px; display: flex; align-items: baseline; justify-content: space-between;
    padding: 0 42px; white-space: nowrap; color: var(--ink);
  }
  .spine-author { font-family: "Cinzel", "Times New Roman", serif; font-size: 22px; }
  .spine-title { font-family: "Cinzel", "Times New Roman", serif; font-size: 22px; }
  .spine-title .script { font-family: "Allura", cursive; font-size: 34px; text-transform: none; margin: 0 6px; }

  /* Front cover */
  .front-cover { position: absolute; left: 643px; top: 0; width: 557px; height: 830px; background: var(--ink); }
  .cover-photo {
    position: absolute; left: 2px; top: 0; width: 555px; height: 436px;
    background:
      radial-gradient(ellipse 45% 40% at 58% 12%, #f4f0d0 0%, rgba(230,220,150,0.6) 40%, rgba(0,0,0,0) 75%),
      radial-gradient(ellipse 40% 45% at 95% 30%, rgba(170,190,70,0.75), rgba(0,0,0,0) 70%),
      linear-gradient(180deg, #5d7d84 0%, #3d5861 40%, #23323a 70%, #0a0d10 100%);
  }
  .cover-photo::after {
    content: ""; position: absolute; left: 0; right: 0; bottom: 0; height: 50px;
    background: linear-gradient(180deg, rgba(0,0,0,0), var(--ink));
  }
  .front-title {
    position: absolute; left: 0; width: 557px; top: 452px; text-align: center;
    color: var(--gold-light);
  }
  .title-caps {
    display: block; font-family: "Cinzel", "Times New Roman", serif; font-weight: 400;
    font-size: 72px; line-height: 80px; letter-spacing: 1px;
    background: linear-gradient(180deg, var(--gold-light), var(--gold-mid) 60%, var(--gold-deep));
    -webkit-background-clip: text; background-clip: text; color: transparent;
  }
  .title-script-row { display: flex; align-items: center; gap: 12px; padding: 0 16px 0 18px; height: 66px; }
  .title-rule { flex: 1; height: 4px; background: var(--gold-mid); }
  .title-script { font-family: "Allura", cursive; font-size: 64px; line-height: 1; color: var(--gold-light); white-space: nowrap; }
  .author-band {
    position: absolute; left: 3px; top: 742px; width: 554px; height: 84px;
    background: linear-gradient(90deg, var(--band-dark), var(--band-light) 35%, #b89c66 70%, var(--band-dark));
    display: flex; align-items: center; justify-content: center;
  }
  .author-name { font-family: "Cinzel", "Times New Roman", serif; font-size: 58px; color: var(--title-ink); letter-spacing: 1px; }
</style>
</head>
<body>
<div class="cover-wrap">

  <section class="back-cover">
    <p class="back-copy intro">Lorem ipsum dolor sit amet, consectetur adipiscing elit. Integer est sapien, laoreet finibus nulla eu, fermentum mollis orci. Nunc quis mi ac ex sodales lacinia ac ac nunc. Sed dolor augue, euismod aliquam eleifend vitae, lobortis eget arcu. Integer augue nunc, vestibulum eu augue id, ornare ornare tortor. Quisque sit amet dolor ornare arcu luctus vulputate at id sem. Nam ac massa sit amet orci efficitur consectetur. Nunc ullamcorper leo et magna tristique, in fringilla eros fringilla. Orci varius natoque penatibus et magnis dis parturient montes, nascetur ridiculus mus.</p>
    <p class="back-copy details">Vestibulum odio enim, fermentum ut leo id, viverra vehicula ligula. Quisque dapibus dolor purus, at consectetur ipsum fringilla sed. Pellentesque ultricies elit dignissim, convallis quam sed, facilisis augue. Donec congue sem a dolor tincidunt tempor. Quisque elit dolor, porta congue commodo nec, mattis sit amet dolor. Pellentesque tempor diam at quam ultricies rhoncus. Donec ultrices felis turpis, hendrerit commodo mauris rhoncus eu. Donec at scelerisque nibh. Fusce hendrerit sagittis semper.</p>
    <div class="author-photo" role="img" aria-label="Author photo placeholder"></div>
    <p class="back-copy about">Lorem ipsum dolor sit amet, consectetur adipiscing elit. Integer est sapien, laoreet finibus nulla eu, fermentum mollis orci. Nunc quis mi ac ex sodales lacinia ac ac nunc. Sed dolor augue, euismod aliquam eleifend vitae, lobortis eget arcu. Integer augue nunc, vestibulum eu augue id, ornare ornare tortor. Quisque sit amet</p>
    <div class="isbn-block" aria-hidden="true"></div>
  </section>

  <section class="spine">
    <div class="spine-text">
      <span class="spine-author">AUTHOR NAME</span>
      <span class="spine-title">PLANTING <span class="script">gardens after every</span> STORM</span>
    </div>
  </section>

  <section class="front-cover">
    <div class="cover-photo" role="img" aria-label="Photo of a man in a suit standing at a fork in a misty forest road, with signposts pointing to an old life and a new life"></div>
    <h1 class="front-title">
      <span class="title-caps">PLANTING</span>
      <span class="title-script-row">
        <span class="title-rule"></span>
        <span class="title-script">gardens after every</span>
        <span class="title-rule"></span>
      </span>
      <span class="title-caps">STORM</span>
    </h1>
    <div class="author-band"><span class="author-name">AUTHOR NAME</span></div>
  </section>

</div>
</body>
</html>
```